Word template Letterhead for Australian Law Firm

We are a small law firm based in Manly, NSW, Australia. We have had a new logo designed for us and wish to freshen up the appearance of our letterhead. We require the letterhead to be in a word document that we can type over. This will not be a ‘printed’ letterhead because we send the majority of our correspondence via email. We would like to see a few options. We have attached our previous letterhead as well as the artwork for our new logo. We like the idea of a watermark across the bottom of the letter but the watermark must stay in place and we must be able to type over it. We are open to some colour throughout the letterhead because the majority of our correspondence is sent electronically. We also use electronic signatures. I have uploaded an example of this.The letterhead must include:-1. Our address details – including our phone number, physical address, website address etc. These details can be found on the copy of our previous letterhead;2. ABN Number;3. The words ‘Brevicor (NSW) Pty Ltd ACN 482 731 058 trading as Shipton & AssociatesLiability limited by a scheme approved under Professional Standards Legislation. The letterhead does not need to include the names and qualifications of the people working at the firm. Thank you.

Target Market(s)

Clients and other parties

Industry/Entity Type

Law Firm

Font styles to use
Other font styles liked:
• raleway, montserrat

Colors

Designer to choose colors to be used in the design.

Requirements
Must have
• Certain wording - please see project description.
• Must be a word document and must be able to type over the watermark etc.
Nice to have
• Watermark at the bottom of the letter.

```html
<!DOCTYPE html>
<html lang="en">
<head>
<meta charset="utf-8">
<title>Kervell &amp; Associates Letterhead</title>
<link href="https://fonts.googleapis.com/css2?family=Montserrat:wght@400;500;600;700&display=swap" rel="stylesheet">
<style>
  :root {
    --backdrop: #e9eaec;
    --paper: #ffffff;
    --ink: #1d1d1f;
    --ink-soft: #3a3a3d;
    --brand-navy: #3a3f8f;
    --wash-blue: #dfe3f7;
    --wash-gold: #f3ecd6;
    --badge-dark: #1b1b1f;
  }
  * { box-sizing: border-box; margin: 0; padding: 0; }
  html, body {
    width: 1200px; height: 1200px; overflow: hidden;
    background: var(--backdrop);
    font-family: "Montserrat", Arial, sans-serif;
    color: var(--ink);
  }
  .letterhead {
    position: absolute; left: 204px; top: 40px;
    width: 792px; height: 1120px;
    background: var(--paper);
    box-shadow: 0 6px 18px rgba(0,0,0,0.18);
  }
  .brand {
    position: absolute; left: 72px; top: 96px;
    display: flex; align-items: center; gap: 12px;
  }
  .brand-mark {
    width: 34px; height: 34px; border-radius: 50%;
    background: var(--brand-navy);
  }
  .brand-name {
    font-size: 19px; font-weight: 600; color: var(--brand-navy);
  }
  .contact {
    position: absolute; right: 43px; top: 56px;
    text-align: right; font-size: 13px; line-height: 18px; color: var(--ink-soft);
    font-style: normal;
  }
  .contact .web { font-weight: 700; color: var(--ink); }
  .recipient {
    position: absolute; left: 72px; top: 258px;
    font-size: 13.5px; line-height: 18px;
  }
  .body {
    position: absolute; left: 72px; top: 388px; width: 676px;
    font-size: 13.5px; line-height: 20px; text-align: justify; color: var(--ink-soft);
  }
  .body p { margin-bottom: 23px; }
  .body .salutation { margin-bottom: 26px; color: var(--ink); }
  .body strong { color: var(--ink); font-weight: 700; }
  .signoff {
    position: absolute; left: 72px; top: 760px;
    font-size: 13px; line-height: 18px;
  }
  .signature {
    width: 80px; height: 36px; margin: 4px 0 2px;
    background: linear-gradient(90deg, #cfd0d6, #e8e9ee);
    border-radius: 4px;
  }
  .signoff .name { font-weight: 700; }
  .watermark { position: absolute; left: 300px; top: 740px; }
  .accreditation {
    position: absolute; left: 628px; top: 890px;
    width: 128px; height: 128px; border-radius: 50%;
    background: var(--badge-dark);
  }
  .legal {
    position: absolute; left: 0; right: 0; top: 1048px;
    text-align: center; font-size: 13px; line-height: 19px; color: var(--ink-soft);
  }
  .legal strong { color: var(--ink); font-weight: 700; }
</style>
</head>
<body>
<main class="letterhead">
  <header>
    <div class="brand">
      <div class="brand-mark"></div>
      <div class="brand-name">Kervell &amp; Associates</div>
    </div>
    <address class="contact">
      SUITE 4, 18 CORELLA LANE MANLY<br>
      NSW 2095<br>
      T: (02) 9410 3827<br>
      F: (02) 9410 3828<br>
      E: office@brevicorlaw.com.au<br>
      ABN: 41 482 731 058<br>
      <span class="web">www.kervellassociates.com.au</span>
    </address>
  </header>

  <section class="recipient">
    To,<br>
    Managing Director<br>
    Tarnwell Properties<br>
    84, Quillon Street<br>
    Harbour, SA 5005
  </section>

  <section class="body">
    <p class="salutation">Dear Hale,</p>
    <p><strong>Lorem Ipsum</strong> is simply dummy text of the printing and typesetting industry. Lorem Ipsum has been the industry's standard dummy text ever since the 1500s, when an unknown printer took a galley of type and scrambled it to make a type specimen book. It has survived not only five centuries, but also the leap into electronic typesetting, remaining essentially unchanged.</p>
    <p><strong>Lorem Ipsum</strong> is simply dummy text of the printing and typesetting industry. Lorem Ipsum has been the industry's standard dummy text ever since the 1500s.</p>
  </section>

  <svg class="watermark" width="470" height="290" viewBox="0 0 470 290" aria-hidden="true">
    <defs>
      <radialGradient id="wash" cx="50%" cy="50%" r="50%">
        <stop offset="0%" stop-color="var(--wash-blue)" stop-opacity="0.9"/>
        <stop offset="70%" stop-color="var(--wash-gold)" stop-opacity="0.5"/>
        <stop offset="100%" stop-color="#ffffff" stop-opacity="0"/>
      </radialGradient>
    </defs>
    <circle cx="220" cy="150" r="140" fill="url(#wash)"/>
  </svg>

  <section class="signoff">
    Thanks and regards,
    <div class="signature" role="img" aria-label="Electronic signature"></div>
    <div class="name">Dorian Hale</div>
    <div>Founder &amp; CEO</div>
  </section>

  <div class="accreditation" role="img" aria-label="Accreditation badge"></div>

  <footer class="legal">
    <strong>Brevicor (NSW) Pty Ltd</strong> ACN 482 731 058 trading as Kervell &amp; Associates Liability limited<br>
    by a scheme approved under Professional Standards Legislation
  </footer>
</main>
</body>
</html>
```